Talbrin Business Cards

Front and back. Simon Kavelle MBA is the CEO of Talbrin Homes. Black white and grays. Logo and cool design.

Target Market(s)

Professional lenders and investors

Industry/Entity Type

Real estate developer. NO HOUSES OR ROOFS

Contact Information for Business Card

Logo, name and unique design. Front and back. Simon Kavelle MBA is the CEO of Talbrin Homes. Black white and grays. Logo and cool design.

Font styles to use
Sans Serif

Colors

Designer to choose only greyscale colors for use in the design.

Requirements
Must have
• Cool look. Not the same card I could design.
Nice to have
• Something memorable
Should not have
• Basic

```html
<!DOCTYPE html>
<html lang="en">
<head>
<meta charset="utf-8">
<title>Talbrin Homes – Business Cards</title>
<link rel="stylesheet" href="https://fonts.googleapis.com/css2?family=Montserrat:wght@400;500;700;800&display=swap">
<style>
  :root {
    --bg: #d9d9d9;
    --ink: #0a0a0a;
    --paper: #ffffff;
    --shadow: rgba(0,0,0,0.28);
  }
  * { margin: 0; padding: 0; box-sizing: border-box; }
  html, body {
    width: 1200px; height: 798px; overflow: hidden;
    background: var(--bg);
    font-family: "Montserrat", Arial, sans-serif;
  }
  .canvas { position: relative; width: 1200px; height: 798px; }
  .card {
    position: absolute;
    width: 560px; height: 320px;
    box-shadow: 0 10px 28px var(--shadow);
  }
  .card--back { left: 50px; top: 90px; background: var(--ink); }
  .card--front { left: 590px; top: 388px; background: var(--paper); color: var(--ink); }

  .brand-name {
    position: absolute;
    font-weight: 800;
    letter-spacing: -1px;
    white-space: nowrap;
  }
  .card--back .brand-name {
    color: var(--paper);
    font-size: 64px;
    left: 0; right: 0; top: 118px;
    text-align: center;
  }
  .card--front .brand-name {
    color: var(--ink);
    font-size: 32px;
    right: 28px; top: 26px;
  }

  .holder { position: absolute; left: 32px; top: 112px; }
  .holder__name { font-weight: 800; font-size: 19px; letter-spacing: 0.3px; white-space: nowrap; }
  .holder__title { font-weight: 400; font-size: 14px; margin-top: 2px; }

  .address {
    position: absolute; right: 28px; top: 150px;
    font-size: 14px; font-weight: 500; line-height: 1.45; text-align: right;
    white-space: nowrap;
  }

  .contacts { position: absolute; left: 32px; bottom: 26px; list-style: none; }
  .contacts li {
    display: flex; align-items: center; gap: 12px;
    font-size: 15px; font-weight: 500; height: 28px; white-space: nowrap;
  }
  .contacts svg { width: 20px; height: 20px; flex: none; }
</style>
</head>
<body>
<main class="canvas">
  <section class="card card--back" aria-label="Card back">
    <div class="brand-name">Talbrin Homes</div>
  </section>

  <section class="card card--front" aria-label="Card front">
    <div class="brand-name">Talbrin Homes</div>

    <div class="holder">
      <div class="holder__name">SIMON KAVELLE MBA</div>
      <div class="holder__title">CEO</div>
    </div>

    <div class="address">41-07 Larkmoor Ave<br>Brenfield, NY</div>

    <ul class="contacts">
      <li>
        <svg viewBox="0 0 20 20" aria-hidden="true">
          <circle cx="10" cy="10" r="10" fill="#0a0a0a"/>
          <path d="M6 7.5c0-1 1-1.6 4-1.6s4 .6 4 1.6v.8h-2V7.6H8v.7H6z M7 9h6l1 4H6z" fill="#fff"/>
        </svg>
        555-014-2368
      </li>
      <li>
        <svg viewBox="0 0 20 20" aria-hidden="true">
          <circle cx="10" cy="10" r="10" fill="#0a0a0a"/>
          <rect x="5" y="6.5" width="10" height="7" fill="#fff"/>
          <path d="M5 6.5l5 4 5-4" fill="none" stroke="#0a0a0a" stroke-width="1"/>
        </svg>
        info@talbrinhomes.com
      </li>
      <li>
        <svg viewBox="0 0 20 20" aria-hidden="true">
          <circle cx="10" cy="10" r="10" fill="#0a0a0a"/>
          <circle cx="10" cy="10" r="5" fill="none" stroke="#fff" stroke-width="1.2"/>
          <path d="M5 10h10M10 5c-2.5 3-2.5 7 0 10M10 5c2.5 3 2.5 7 0 10" fill="none" stroke="#fff" stroke-width="1"/>
        </svg>
        www.talbrinhomes.com
      </li>
    </ul>
  </section>
</main>
</body>
</html>
```